Paper Orchards (instructional dating book)

Title: Paper Orchards
Subtitle: Ways to charm a stranger across any crowded room
Author: R.J. Pollard
I'm seeking the title to be central with the subtitle underneath and the author slightly lower and to the left. Perhaps a border or two around the font. I thought the background could look aged (off color and old textured paper) and the background slightly punched into the texture like a typewriter has been used. I imagine it something like an old Fenwright playbook or 1940s morse code manual. Many thanks!

Target Market(s)

18 to 45 year old single people

Industry/Entity Type

Dating

Font styles to use
Serif

Requirements
Must have
• Text with border or two
Nice to have
• Traditional feel. The book is instructional.
Should not have
• Too much color or flair

```html
<!DOCTYPE html>
<html lang="en">
<head>
<meta charset="utf-8">
<title>Paper Orchards — Cover</title>
<link href="https://fonts.googleapis.com/css2?family=Tinos&display=swap" rel="stylesheet">
<style>
  :root {
    --page-bg: #ffffff;
    --cover-white: #ffffff;
    --frame-brown: #5a4632;
    --ink-brown: #6a5038;
    --paper-light: #e6cfa8;
    --paper-mid: #d9b98a;
    --paper-dark: #c99a5c;
    --paper-edge: #b98a52;
  }
  * { margin: 0; padding: 0; box-sizing: border-box; }
  html, body {
    width: 1200px;
    height: 1135px;
    overflow: hidden;
    background: var(--page-bg);
  }
  .canvas {
    position: relative;
    width: 1200px;
    height: 1135px;
  }
  .cover {
    position: absolute;
    left: 240px;
    top: 38px;
    width: 720px;
    height: 1060px;
    background: var(--cover-white);
    box-shadow: 0 2px 10px rgba(0,0,0,0.12);
  }
  .cover-frame {
    position: absolute;
    inset: 6px;
    border: 2px solid var(--frame-brown);
  }
  .paper-sheet {
    position: absolute;
    left: 30px;
    right: 30px;
    top: 66px;
    bottom: 66px;
    background: var(--paper-mid);
    box-shadow: 0 1px 4px rgba(0,0,0,0.25);
  }
  .paper-sheet.back-one { transform: rotate(-0.9deg) translate(6px, -4px); background: var(--paper-edge); }
  .paper-sheet.back-two { transform: rotate(0.7deg) translate(-4px, 5px); background: var(--paper-dark); }
  .paper-sheet.front {
    background:
      radial-gradient(ellipse at 85% 4%, rgba(201,138,60,0.75) 0%, rgba(201,138,60,0) 22%),
      radial-gradient(ellipse at 10% 60%, rgba(190,140,80,0.35) 0%, rgba(190,140,80,0) 35%),
      radial-gradient(ellipse at 50% 45%, var(--paper-light) 0%, var(--paper-mid) 70%, var(--paper-dark) 100%);
  }
  .cover-text {
    position: absolute;
    left: 30px;
    right: 30px;
    top: 66px;
    bottom: 66px;
    text-align: center;
    font-family: "Tinos", "Times New Roman", serif;
    color: var(--ink-brown);
  }
  .title {
    position: absolute;
    left: 0; right: 0;
    top: 215px;
    font-size: 84px;
    font-weight: 400;
    line-height: 1.3;
    letter-spacing: 0.24em;
    text-shadow: 0 1px 0 rgba(255,240,210,0.5), 0 -1px 0 rgba(70,45,20,0.35);
  }
  .subtitle {
    position: absolute;
    left: 60px; right: 60px;
    top: 565px;
    font-size: 30px;
    line-height: 1.3;
  }
  .author {
    position: absolute;
    left: 0; right: 40px;
    top: 850px;
    font-size: 29px;
    letter-spacing: 0.04em;
    text-transform: uppercase;
  }
</style>
</head>
<body>
  <main class="canvas">
    <section class="cover" aria-label="Book cover: Paper Orchards">
      <div class="cover-frame"></div>
      <div class="paper-sheet back-one"></div>
      <div class="paper-sheet back-two"></div>
      <div class="paper-sheet front" role="img" aria-label="Aged, stained parchment paper texture"></div>
      <div class="cover-text">
        <h1 class="title">Paper<br>Orchards</h1>
        <p class="subtitle">Ways to charm a stranger across any crowded room</p>
        <p class="author">R.J. Pollard</p>
      </div>
    </section>
  </main>
</body>
</html>
```